Redesign Business Cards, Attached

Please read instructions carefully. If you have any questions send a message before submitting your ONE design. Please redesign attached business cards. Double sided. Use same content and descriptions. Use black, silver, crimson red and gold colors. My only issue with the attached design is the background colors. I like the layout as-is. I can provide the individual pictures on the back side later. Do not submit more than one design. One submission shall include both front and back. Do not submit front and back separately. A second project will be launched to create a matching post card after completion of this.
Industry/Entity Type
see description and attachments.
Contact Information for Business Card
Requirements
Must have
- see description and attachments.
Nice to have
Should not have

```html
<!DOCTYPE html>
<html lang="en">
<head>
<meta charset="utf-8">
<title>Harbor Helm Business Card – Front and Back</title>
<link rel="stylesheet" href="https://fonts.googleapis.com/css2?family=Montserrat:wght@400;500;800&family=Oswald:wght@500&display=swap">
<style>
  :root {
    --crimson: #6e0202;
    --crimson-deep: #5a0000;
    --gold: #d4a51c;
    --ink: #111111;
    --grey: #3c3c3c;
    --white: #ffffff;
    --table: #3a3a3a;
  }
  * { margin: 0; padding: 0; box-sizing: border-box; }
  html, body { width: 1200px; height: 1200px; overflow: hidden; }
  body {
    background: var(--table);
    font-family: "Montserrat", Arial, sans-serif;
    position: relative;
  }
  .card {
    position: absolute;
    left: 180px;
    width: 840px;
    height: 480px;
    border-radius: 30px;
    overflow: hidden;
  }
  .card-front { top: 60px; background: var(--white); }
  .card-back { top: 600px; background: var(--crimson); }

  .front-wave { position: absolute; inset: 0; }

  .identity {
    position: absolute;
    left: 60px;
    top: 140px;
  }
  .identity-name {
    color: var(--crimson);
    font-weight: 800;
    font-size: 38px;
    letter-spacing: 0.5px;
    line-height: 1;
  }
  .identity-role {
    color: var(--grey);
    font-weight: 400;
    font-size: 19px;
    line-height: 1.2;
    margin-top: 8px;
    letter-spacing: 0.3px;
  }
  .contact-list {
    list-style: none;
    margin-top: 26px;
  }
  .contact-item {
    display: flex;
    align-items: center;
    gap: 14px;
    color: var(--ink);
    font-size: 23px;
    line-height: 1.35;
  }
  .contact-icon { width: 24px; height: 24px; flex: none; }

  .brand {
    position: absolute;
    display: flex;
    align-items: center;
    gap: 14px;
    font-weight: 800;
    line-height: 1.1;
    text-transform: uppercase;
  }
  .brand-mark { border-radius: 50%; flex: none; }
  .brand-front { right: 60px; top: 110px; color: var(--ink); font-size: 22px; }
  .brand-front .brand-mark { width: 26px; height: 26px; background: var(--gold); }
  .brand-back {
    left: 50%; top: 120px; transform: translateX(-50%);
    color: var(--white); font-size: 36px; text-align: left;
  }
  .brand-back .brand-mark { width: 40px; height: 40px; background: var(--gold); }
  .brand-sub { display: block; font-size: 0.55em; letter-spacing: 1px; }

  .badge {
    position: absolute;
    border-radius: 50%;
  }
  .badge-council { left: 70px; top: 130px; width: 130px; height: 130px; background: #1e4f9c; border: 6px solid #2ab3c6; }
  .badge-veteran { right: 80px; top: 40px; width: 110px; height: 110px; background: #1d2f7a; border: 6px solid #d4222a; }

  .services {
    position: absolute;
    left: 40px;
    right: 40px;
    bottom: 44px;
    font-family: "Oswald", "Arial Narrow", sans-serif;
    font-weight: 500;
    color: var(--white);
    font-size: 17px;
    line-height: 1.55;
    text-transform: uppercase;
    text-align: center;
    letter-spacing: 0.2px;
  }
  .services .dot { color: var(--gold); padding: 0 6px; }
</style>
</head>
<body>

<section class="card card-front" aria-label="Business card front">
  <svg class="front-wave" viewBox="0 0 840 480" preserveAspectRatio="none" aria-hidden="true">
    <path d="M0,400 C220,430 420,360 580,250 C690,175 780,150 840,130 L840,150 C780,170 700,200 590,275 C430,385 220,450 0,420 Z" fill="var(--gold)"/>
    <path d="M0,430 C230,460 440,390 600,285 C700,215 780,185 840,170 L840,480 L0,480 Z" fill="var(--crimson)"/>
  </svg>

  <div class="brand brand-front">
    <span class="brand-mark"></span>
    <span>Harbor Helm<span class="brand-sub">Boat Training &amp; Charters</span></span>
  </div>

  <div class="identity">
    <h1 class="identity-name">DANA R. HOLLOWAY</h1>
    <p class="identity-role">USCG LICENSED CAPTAIN<br>CERTIFIED INSTRUCTOR</p>
    <ul class="contact-list">
      <li class="contact-item">
        <svg class="contact-icon" viewBox="0 0 24 24" aria-hidden="true"><path fill="var(--crimson)" d="M6.6 10.8a15 15 0 0 0 6.6 6.6l2.2-2.2c.3-.3.7-.4 1-.2 1.1.4 2.3.6 3.6.6.6 0 1 .4 1 1V20c0 .6-.4 1-1 1A17 17 0 0 1 3 4c0-.6.4-1 1-1h3.5c.6 0 1 .4 1 1 0 1.3.2 2.5.6 3.6.1.3 0 .7-.2 1z"/></svg>
        TEXT (555) 014-2287
      </li>
      <li class="contact-item">
        <svg class="contact-icon" viewBox="0 0 24 24" aria-hidden="true"><g fill="none" stroke="var(--crimson)" stroke-width="2"><circle cx="12" cy="12" r="10"/><ellipse cx="12" cy="12" rx="4.5" ry="10"/><path d="M2 12h20M4 7h16M4 17h16"/></g></svg>
        www.harborhelm.com
      </li>
      <li class="contact-item">
        <svg class="contact-icon" viewBox="0 0 24 24" aria-hidden="true"><rect x="2" y="5" width="20" height="14" fill="var(--crimson)"/><path d="M2 5l10 8 10-8" fill="none" stroke="var(--white)" stroke-width="1.6"/></svg>
        service@harborhelm.com
      </li>
    </ul>
  </div>
</section>

<section class="card card-back" aria-label="Business card back">
  <div class="badge badge-council" role="img" aria-label="Safe boating council instructor badge"></div>
  <div class="badge badge-veteran" role="img" aria-label="Veteran owned business member badge"></div>

  <div class="brand brand-back">
    <span class="brand-mark"></span>
    <span>Harbor Helm<span class="brand-sub">Boat Training &amp; Charters</span></span>
  </div>

  <p class="services">
    <span class="dot">•</span>Hands-on boat training<span class="dot">•</span>Introduction to power boating<span class="dot">•</span>Precision docking &amp; boat handling<span class="dot">•</span>Open water advanced handling<br>
    <span class="dot">•</span>Island anchoring<span class="dot">•</span>Open water advanced maneuvers<span class="dot">•</span>Coastal navigation<span class="dot">•</span>Captaining / piloting service for your outings
  </p>
</section>

</body>
</html>
```